Byte Wardens Inc. IT Services and Sales

We need a new business card design for our new company. We have a current logo but are open and encourage any redesigns.

Byte Wardens is derived in our history from computer gaming. (NovaFront References, SURGE UNLEASHED!!!). We as a group have been together since high school (2002). Our friendships brought us together and now we are all business partners providing IT Support and Consultation Services ranging from fixing small issues like printers, home networking, pc building to custom application development and managed cloud and it networks for our clients.
We would like our design to communicate that we strive to be the best (we are born gamers and have a highly competitive instinct) and offer solutions to problems that other companies just simply say we can't do it. We are always looking to go above and beyond for our clients, learning our clients business and figuring out ways to help them make more money by optimizing the way they do business, offering solutions so they can grow their business and helping everyone utilize the technology they have or advise them with the technology they need to succeed.

Attached are things we have on our computers and logo's we have used.
One is a desktop background
while the other should be our logo.

Again, we are open to and encourage any logo redesigns in hope things can help with the direction we are looking into.

Please add a place for email as our current cards have no email and it makes us very sad.
Updates

Hi All,

Just wanted to say thank you for all those who submitted a design. We've updated our project to include the fact that we are open and encourage a logo redesign. Also, this project is now committed to payment.

Target Market(s)

We will be handing these out to all our future business prospects. Prospects are usually business owners that can be in any industry. They look to us to be cutting edge or professional.

Industry/Entity Type

High School

Requirements
Must have
• name, title, work, fax, and cell phone, address and email

```html
<!DOCTYPE html>
<html lang="en">
<head>
<meta charset="utf-8">
<title>Byte Wardens – Business Card</title>
<link rel="stylesheet" href="https://fonts.googleapis.com/css2?family=Open+Sans:wght@400;600;700&display=swap">
<style>
  :root {
    --page: #e9e7e4;
    --card-dark: #141414;
    --card-mid: #2a2a2a;
    --accent: #f07a3c;
    --accent-deep: #e2501f;
    --text-light: #f2f2f2;
    --text-muted: #cfcfcf;
  }
  * { box-sizing: border-box; margin: 0; padding: 0; }
  html, body { width: 1200px; height: 800px; overflow: hidden; }
  body {
    background: var(--page);
    font-family: "Open Sans", Arial, sans-serif;
    position: relative;
  }
  .card {
    position: absolute;
    overflow: hidden;
    box-shadow: 0 14px 30px rgba(0,0,0,.35);
  }
  .card-texture {
    position: absolute; inset: 0;
    background: radial-gradient(ellipse at 40% 30%, var(--card-mid) 0%, var(--card-dark) 75%);
  }

  /* Front: portrait card */
  .card-front { left: 90px; top: 90px; width: 380px; height: 620px; }
  .front-brand {
    position: absolute; left: 150px; top: 140px;
    display: flex; flex-direction: row-reverse; align-items: flex-start; gap: 12px;
    writing-mode: vertical-rl;
  }
  .brand-name {
    font-weight: 600; color: var(--text-light);
    font-size: 56px; letter-spacing: 1px; line-height: 1;
    white-space: nowrap;
  }
  .front-brand .brand-name { margin-top: 100px; }
  .front-services {
    font-weight: 600; color: var(--accent);
    font-size: 14px; letter-spacing: 1px; line-height: 1;
    text-transform: uppercase; white-space: nowrap;
  }

  /* Back: landscape card */
  .card-back { left: 520px; top: 210px; width: 620px; height: 380px; }
  .band-frame { position: absolute; inset: 0; }
  .back-brand {
    position: absolute; right: 84px; top: 34px;
    font-size: 40px;
  }
  .person { position: absolute; left: 34px; top: 100px; }
  .person-name {
    color: var(--accent); font-weight: 700; font-size: 21px;
    text-transform: uppercase; letter-spacing: .5px;
  }
  .person-title { color: var(--text-muted); font-size: 13px; margin-top: 2px; }
  .contact-list { list-style: none; margin-top: 10px; }
  .contact-list li {
    display: flex; align-items: center; gap: 8px;
    color: var(--text-light); font-size: 13px; line-height: 22px;
    white-space: nowrap;
  }
  .contact-icon { width: 14px; height: 14px; flex: none; }
  .address {
    position: absolute; left: 330px; top: 232px;
    color: var(--text-light); font-size: 14px; line-height: 20px;
    font-style: normal; white-space: nowrap;
  }
</style>
</head>
<body>

<section class="card card-front" aria-label="Business card front">
  <div class="card-texture" role="img" aria-label="Dark hexagon mesh background texture"></div>
  <div class="front-brand">
    <span class="brand-name">Byte Wardens</span>
    <span class="front-services">Retail | IT Services | IT Consultation | Marketing</span>
  </div>
</section>

<section class="card card-back" aria-label="Business card back">
  <div class="card-texture" role="img" aria-label="Dark hexagon mesh background texture"></div>
  <svg class="band-frame" viewBox="0 0 620 380" preserveAspectRatio="none" aria-hidden="true">
    <defs>
      <linearGradient id="bandGradient" x1="0" x2="1" y1="0" y2="0">
        <stop offset="0" stop-color="#f28a4c"/>
        <stop offset="1" stop-color="#e4471c"/>
      </linearGradient>
    </defs>
    <path d="M0 310 H560 V0 H620 V380 H0 Z" fill="#1c1c1c"/>
    <path d="M0 300 H548 V0 H576 V326 H0 Z" fill="url(#bandGradient)"/>
  </svg>

  <div class="brand-name back-brand">Byte Wardens</div>

  <div class="person">
    <div class="person-name">Dana Reyes</div>
    <div class="person-title">Director</div>
    <ul class="contact-list">
      <li>
        <svg class="contact-icon" viewBox="0 0 14 14" aria-hidden="true"><rect width="14" height="14" rx="2" fill="var(--accent)"/><path d="M4 3h2l1 2.5-1.2.8a6 6 0 0 0 2 2l.8-1.2L11 8v2a1 1 0 0 1-1 1A7 7 0 0 1 3 4a1 1 0 0 1 1-1z" fill="#1a1a1a"/></svg>
        5550 142 876
      </li>
      <li>
        <svg class="contact-icon" viewBox="0 0 14 14" aria-hidden="true"><rect width="14" height="14" rx="2" fill="var(--accent)"/><rect x="4.5" y="2.5" width="5" height="9" rx="1" fill="#1a1a1a"/></svg>
        5550 198 304
      </li>
      <li>
        <svg class="contact-icon" viewBox="0 0 14 14" aria-hidden="true"><rect width="14" height="14" rx="2" fill="var(--accent)"/><rect x="4" y="2.5" width="6" height="3" fill="#1a1a1a"/><rect x="2.5" y="5.5" width="9" height="5" rx="1" fill="#1a1a1a"/></svg>
        Fax 5550 177 920
      </li>
      <li>
        <svg class="contact-icon" viewBox="0 0 14 14" aria-hidden="true"><rect width="14" height="14" rx="2" fill="var(--accent)"/><rect x="3" y="4" width="8" height="6" fill="#1a1a1a"/><path d="M3 4l4 3 4-3" stroke="var(--accent)" fill="none"/></svg>
        dana@bytewardens.example
      </li>
    </ul>
  </div>

  <address class="address">
    24 Harlow Ln. Westbury<br>Ma. 01620
  </address>
</section>

</body>
</html>
```